Marco T. Vellen Birch Hollow sales specialist

I need a postcard for a mailer to a specific waterfront association, and I want to let them know I just sold THE most premier waterfront on that area, and if they are looking to sell, I am the professional they should call. The photo I uploaded I would like on the card because that is the home I sold. I would like the Phrase : Cove de Lark Sold! some place on the card, as well as all of my contact info and name of our Real Estate Firm.

Here is the name of My Firm and my contact info:\

Tolland Real Estate
Marco T. Vellen
Office 603-555-0142
Cell 603-555-0187
Email Marco@tollandrealestate.net

Industry/Entity Type

Real Estate

Font styles to use
Serif

```html
<!DOCTYPE html>
<html lang="en">
<head>
<meta charset="utf-8">
<title>Looking to sell? — Cove de Lark Sold!</title>
<link rel="stylesheet" href="https://fonts.googleapis.com/css2?family=Gelasio:wght@400;500&family=Bebas+Neue&display=swap">
<style>
  :root {
    --paper: #ffffff;
    --headline-green: #3f6a22;
    --sold-olive: #5e6248;
    --frame-light: #dcdcdc;
    --frame-mid: #c9c9c9;
    --photo-sky: #e4ebe0;
    --photo-pines: #4e6d3a;
    --photo-house: #cfd6cb;
    --photo-lawn: #6f9548;
    --photo-gravel: #ddd0d2;
  }
  * { margin: 0; padding: 0; box-sizing: border-box; }
  html, body {
    width: 1200px;
    height: 930px;
    overflow: hidden;
    background: var(--paper);
  }
  .postcard {
    position: relative;
    width: 1200px;
    height: 930px;
    background: var(--paper);
  }
  .headline {
    position: absolute;
    top: 92px;
    left: 0;
    width: 1200px;
    text-align: center;
    font-family: "Gelasio", Georgia, serif;
    font-weight: 500;
    font-size: 130px;
    line-height: 1.2;
    letter-spacing: 6px;
    color: var(--headline-green);
  }
  .featured-home {
    position: absolute;
    top: 0;
    left: 0;
    width: 1200px;
    height: 930px;
  }
  .agent-contact {
    position: absolute;
    left: 80px;
    top: 846px;
    font-family: "Gelasio", Georgia, serif;
    font-size: 15px;
    line-height: 1.45;
    color: var(--sold-olive);
    font-style: normal;
  }
  .agent-contact .agent-name {
    font-weight: 500;
    color: var(--headline-green);
  }
  .sold-note {
    position: absolute;
    right: 75px;
    top: 862px;
    font-family: "Bebas Neue", "Arial Narrow", sans-serif;
    font-size: 41px;
    line-height: 1;
    letter-spacing: 3px;
    color: var(--sold-olive);
  }
</style>
</head>
<body>
  <main class="postcard">
    <h1 class="headline">Looking to sell?</h1>

    <svg class="featured-home" viewBox="0 0 1200 930">
      <defs>
        <linearGradient id="home-tones" x1="0" y1="0" x2="0" y2="1">
          <stop offset="0" stop-color="var(--photo-sky)"/>
          <stop offset="0.3" stop-color="var(--photo-pines)"/>
          <stop offset="0.5" stop-color="var(--photo-house)"/>
          <stop offset="0.72" stop-color="var(--photo-lawn)"/>
          <stop offset="1" stop-color="var(--photo-gravel)"/>
        </linearGradient>
      </defs>
      <g class="photo-frames">
        <rect x="296" y="322" width="594" height="484" fill="none"
              stroke="var(--frame-light)" stroke-width="18"
              transform="rotate(-3 593 564)"/>
        <rect x="300" y="326" width="594" height="484" fill="none"
              stroke="var(--frame-mid)" stroke-width="14"
              transform="rotate(3 597 568)"/>
      </g>
      <rect class="home-photo" x="296" y="336" width="600" height="468"
            fill="url(#home-tones)" transform="rotate(-2 596 570)"
            role="img" aria-label="Photo of the sold waterfront home: a white two-storey cottage among tall pines with a landscaped garden, boulder and gravel drive"/>
    </svg>

    <address class="agent-contact">
      <span class="agent-name">Marco T. Vellen · Tolland Real Estate</span><br>
      Office 603-555-0142 · Cell 603-555-0187<br>
      Marco@tollandrealestate.net
    </address>

    <p class="sold-note">Cove de Lark Sold!</p>
  </main>
</body>
</html>
```